The Saga of Brisa

I need a design for a two-page spread to open a very long (and fascinating) story about a famous female architect who basically built our very charming village. I've enclosed copy, photo of her, and several images of key buildings.

My present concept (I'm very open to other ideas) is a female hand with a drafting pencil, working on a blue line, with our town's iconic buildings designed by Brisa Thornquist, Ojai, California, gradually coming into view toward the bottom of the page.

The first paragraph of copy (above the byline) should go on the first left-hand page, then the 7,500 story should follow on the right-hand side. But again, just a suggestion.

Our quarterly magazine is universally regarded as having superior, long-form journalism (the Harbor Ledger of California, as someo, but our design execution is weak. We need your help.

Ojai is an affluent, highly artistic community. And our magazine is expanding nationwide to appeal to both tourists and the rising creative class of people who would be drawn to a community like Ojai.

Architect

• Page specs …

8.375" by 10.875" trim
8.875" by 11.375" bleed (.25" all around)
Spread 17.25" by 11.375" bleed.

Copy …
We use Neutra for headlines and cutlines, Berkeley OldStyle for copy, subheads. But I like the idea of using Triforce - the old Crown of Quillmar typeface for the main headline.

```html
<!DOCTYPE html>
<html lang="en">
<head>
<meta charset="utf-8">
<title>The Saga of Brisa</title>
<link rel="stylesheet" href="https://fonts.googleapis.com/css2?family=Cinzel:wght@600&family=Crimson+Text:ital,wght@0,400;0,600;1,400&family=Cormorant+Garamond:wght@400&display=swap">
<style>
  :root {
    --paper: #ffffff;
    --ink: #2b2620;
    --title-red: #c31f26;
    --title-dark: #7d1016;
    --banner-a: #f1c48c;
    --banner-b: #f7e9d8;
    --banner-c: #b9cf9b;
    --banner-d: #e9b7bf;
    --photo-a: #3a3430;
    --photo-b: #d8d0c6;
    --scene-sky: #c9d9ec;
    --scene-mid: #6f8a6a;
    --scene-low: #e6ddd0;
  }
  * { margin: 0; padding: 0; box-sizing: border-box; }
  html, body { width: 1200px; height: 903px; overflow: hidden; background: var(--paper); }
  body { position: relative; font-family: "Crimson Text", Georgia, serif; color: var(--ink); }

  .title-banner {
    position: absolute; left: 20px; top: 0; width: 572px; height: 202px;
    background: linear-gradient(100deg, var(--banner-a) 0%, var(--banner-d) 30%, var(--banner-b) 55%, var(--banner-c) 80%, var(--banner-a) 100%);
  }
  .title-kicker {
    position: absolute; left: 228px; top: 10px;
    font-family: "Cinzel", serif; font-weight: 600; font-size: 34px;
    color: var(--title-red); letter-spacing: 1px;
  }
  .title-main {
    position: absolute; left: 72px; top: 34px;
    font-family: "Cinzel", serif; font-weight: 600; font-size: 128px; line-height: 1;
    color: var(--title-red); letter-spacing: 2px;
  }

  .intro {
    position: absolute; left: 20px; top: 212px; width: 580px;
    font-size: 19.5px; line-height: 26px;
  }

  .section-head {
    position: absolute; left: 20px; top: 368px;
    font-family: "Cormorant Garamond", serif; font-size: 32px; letter-spacing: 0.5px;
  }
  .byline { position: absolute; left: 20px; top: 408px; font-size: 13px; }

  .col { position: absolute; font-size: 14.6px; line-height: 18.2px; }
  .col p { text-indent: 20px; margin-bottom: 8px; }
  .col p.flush { text-indent: 0; }
  .col-a { left: 20px; top: 438px; width: 276px; }
  .col-b { left: 313px; top: 630px; width: 280px; }
  .col-c { left: 612px; top: 622px; width: 278px; }
  .col-d { left: 912px; top: 598px; width: 278px; }
  .dropcap {
    float: left; font-size: 58px; line-height: 44px; margin: 2px 6px 0 0; font-weight: 400;
  }
  .note { text-transform: uppercase; }

  .portrait {
    position: absolute; left: 313px; top: 369px; width: 280px; height: 256px;
    background: radial-gradient(ellipse at 55% 45%, var(--photo-b) 0%, #8e8580 45%, var(--photo-a) 100%);
  }
  .town-scene {
    position: absolute; left: 612px; top: 0; width: 578px; height: 596px;
    background: linear-gradient(180deg, var(--scene-sky) 0%, #eef1f6 25%, var(--scene-mid) 50%, #c7b39b 70%, var(--scene-low) 85%, #b9b4ad 100%);
  }

  .jump {
    position: absolute; right: 18px; top: 866px;
    font-family: "Crimson Text", serif; font-weight: 600; font-style: italic; font-size: 20px;
    display: flex; align-items: center; gap: 10px;
  }
</style>
</head>
<body>
  <div class="title-banner" role="img" aria-label="Soft wash of autumn trees and a building front behind the headline"></div>
  <div class="title-kicker">THE SAGA OF</div>
  <div class="title-main">BRISA</div>

  <p class="intro">Ojai didn’t take its present form through gradual changes. Instead, it was through several phases of what biologists call “punctuated equilibrium.” First, the fire of 1916 left a clean slate for Walter Ashcombe Greer and his merry band of civic pioneers and philanthropists. Then, the Hollywood Blacklist brought Ojai another. Her name was Brisa Thornquist. This is her story.</p>

  <h2 class="section-head">BRISA’S WORLD</h2>
  <div class="byline">By Marian Holloway Pike</div>

  <div class="col col-a">
    <p class="flush"><span class="dropcap">F</span>ew individuals have left so many indelible marks on the Ojai area landscape as architect Brisa Thornquist, a supreme talent, a great wit and a dear friend. She and I became acquainted through our mutual support of Ventura County Supervisor Nora Ellison Fairbank. Brisa, “citizen warrior” Greta Vance, Louise Amberg — county Counsel for Ventura County, the first woman in the state to hold such a position <span class="note">(this seems out of place in a story about Brisa Thornquist)</span> — and I would travel from Ojai to wherever the “Friends of Nora” were meeting and, in the process, became great friends.</p>
    <p>Before long, we became “Ladies Who Lunch,” whenever we could work it into our schedules. It was in 1993, when Brisa, Vice President (Vice Chair? Don’t think commission has VP, but you’d know better than I) of the Ojai Historic Preservation Commission, suggested I join her on the commission — not because I knew anything about history, preservation, or city law, but because she said she would have much more</p>
  </div>

  <div class="portrait" role="img" aria-label="Black and white portrait photograph of the architect"></div>

  <div class="col col-b">
    <p class="flush">fun with me on board. Now, for the rest of her story.</p>
    <p>Brisa’s creations in Ojai are lived in, learned in, worked in, prayed in and crossed over. But I didn’t realize how little I knew about Brisa until after her death in 1996, when I was asked to give a talk about her life; research led me to discover her roots, her childhood, her marriage to the equally talented Daniel Thornquist — and her fabulous career.</p>
    <p class="note">We could use more description about Brisa’s work and its meaning to Ojai before launching</p>
  </div>

  <div class="town-scene" role="img" aria-label="Hand with drafting pencil above a blueprint fading into town buildings, an arcade and a lit hillside building at dusk"></div>

  <div class="col col-c">
    <p class="flush note">into the old country.</p>
    <p>Consider, for example, the story of her parents and the precarious life they lived in Lithuania and Belarus. Simna, Lithuania, the home of Brisa’s mother, Hanna Rasnova, was about two hours out of Vilnius — since the 14th century, the center of Jewish culture and learning. But by the time of Hanna’s birth in 1892, Lithuanians had been forbidden to speak their own language and Jews were forbidden to own land, reduced to living in ghettos and subject to periodic pogroms of Czarist Russia. Hanna, orphaned at an early age, was living with her Tante Feige.</p>
  </div>

  <div class="col col-d" style="top:622px">
    <p>About 200 miles away, in Belarus, the same sort of persecution was underway, a period of intense "Russification." Brisa’s father, Berel Lomsky, who was living with his widowed mother and apprenticed to a hat-maker, was stopped by the police on one of his deliveries. A note was discovered in the hat: "Come to meeting tonight." With that startling discovery, as well as the threat of enforced service in the Czar’s Army, Berel and his mother decided it was time for him to leave for the land of opportunity. He was 16 years of age.</p>
    <p>On the way, he and a cousin stopped in to</p>
  </div>

  <div class="jump">
    <svg width="30" height="16" viewBox="0 0 30 16" aria-hidden="true">
      <path d="M2 8 H26 M19 2 L27 8 L19 14" fill="none" stroke="#2b2620" stroke-width="1.6"/>
    </svg>
    <span>P. 23</span>
  </div>
</body>
</html>
```